Financial Advisor Resource Firm needs business card design

Need business card design for company in Omaha NE called Tallowbrook Partners. We provide resources to financial advisors....workshop programs, retirement analysis, and insurance planning. I would like to see designs that use grays, greens, black, and white colors. The final design should communicate 'collaboration' and be simple yet attractive to financial planning clients. I will attached our logo and another picture of a puzzle piece coming together. I would like the incorporate the puzzle picture somehow, maybe on the back somehow, with color or just the gray scale....OR, the picture be the front of the card with 'Tallowbrook' definition on it (see upload) and then company logo, employee name, title, address on the back (see ppt uploaded). The following disclosure needs to be included somewhere- Advisory services offered through Marlowe Ridge Advisors, LLC.
Updates

I uploaded a svg and ai file of the logo

Target Market(s)

Financial planning clients and financial advisors....so pretty diverse age range of about 40-70.

Industry/Entity Type

Financial Planning

Contact Information for Business Card

Dennis K. Holloway, MBA
Founder/President
5727 E. Larkspur Avenue
Suite 418
Omaha, NE 68297
Phone- (402) 555-0147
Cell- (402) 555-0183
Fax- (402) 555-0129
email- dennis@tallowbrookgroup.example
web address- www.tallowbrookgroup.example

Colors
1b1b1b
474747
d3d3d3
ffffff
9bcb3c
abd036

Requirements
Must have
• Must include logo provided, must be 2 sided, and must have disclosure...all of these items listed in project description

```html
<!DOCTYPE html>
<html lang="en">
<head>
<meta charset="utf-8">
<title>Tallowbrook Partners – Business Card</title>
<link href="https://fonts.googleapis.com/css2?family=Roboto:wght@400;500;700&display=swap" rel="stylesheet">
<style>
  :root {
    --brand-green: #8bc43f;
    --accent-green: #9bcb3c;
    --ink: #1b1b1b;
    --charcoal: #2f2f2f;
    --mid-gray: #474747;
    --light-gray: #d3d3d3;
    --paper: #ffffff;
    --black: #000000;
  }
  * { margin: 0; padding: 0; box-sizing: border-box; }
  html, body { width: 1200px; height: 1200px; overflow: hidden; }
  body {
    background: var(--brand-green);
    font-family: "Roboto", Arial, sans-serif;
    position: relative;
  }
  .card {
    position: absolute;
    top: 440px;
    width: 550px;
    height: 321px;
    overflow: hidden;
  }
  .card--front { left: 50px; background: var(--black); }
  .card--back { left: 600px; background: var(--paper); }

  /* Front */
  .front-wordmark {
    position: absolute;
    left: 0; right: 0; top: 136px;
    text-align: center;
    color: var(--paper);
    font-size: 32px;
    font-weight: 500;
    letter-spacing: 1px;
  }
  .front-url {
    position: absolute;
    left: 0; right: 0; top: 236px;
    text-align: center;
    color: var(--accent-green);
    font-size: 12px;
    letter-spacing: 3.2px;
  }
  .disclosure {
    position: absolute;
    left: 0; right: 0; bottom: 16px;
    text-align: center;
    color: var(--light-gray);
    font-size: 9px;
    letter-spacing: 0.3px;
  }

  /* Back */
  .photo-circle {
    position: absolute;
    left: 290px; top: 22px;
    width: 302px; height: 302px;
    border-radius: 50%;
    background: radial-gradient(circle at 65% 55%, #5a5a5a 0%, #8d8d8d 40%, #c9c9c9 70%, #f2f2f2 100%);
  }
  .back-wordmark {
    position: absolute;
    left: 24px; top: 50px;
    color: var(--ink);
    font-size: 25px;
    font-weight: 500;
    letter-spacing: 0.5px;
  }
  .name-band {
    position: absolute;
    left: 21px; right: 0; top: 119px;
    height: 26px;
    background: var(--accent-green);
  }
  .name {
    position: absolute;
    left: 26px; top: 120px;
    color: var(--paper);
    font-size: 19px;
    font-weight: 700;
    line-height: 24px;
  }
  .title {
    position: absolute;
    left: 26px; top: 150px;
    color: var(--ink);
    font-size: 16px;
    font-weight: 700;
  }
  .address {
    position: absolute;
    left: 26px; top: 198px;
    color: var(--ink);
    font-size: 12.5px;
    line-height: 17px;
  }
  .contact-row {
    position: absolute;
    left: 26px;
    display: flex;
    align-items: center;
    gap: 14px;
    font-size: 12.5px;
  }
  .contact-row--phones { top: 253px; color: var(--ink); }
  .contact-bar {
    position: absolute;
    left: 0; top: 275px;
    width: 405px; height: 24px;
    background: var(--charcoal);
  }
  .contact-row--bar { top: 279px; color: var(--paper); }
  .contact-item { display: flex; align-items: center; gap: 3px; }
  .contact-icon { width: 12px; height: 12px; fill: var(--accent-green); }
</style>
</head>
<body>

<section class="card card--front" aria-label="Card front">
  <div class="front-wordmark">Tallowbrook Partners</div>
  <div class="front-url">www.tallowbrookgroup.example</div>
  <div class="disclosure">Advisory services offered through Marlowe Ridge Advisors, LLC</div>
</section>

<section class="card card--back" aria-label="Card back">
  <div class="photo-circle" role="img" aria-label="Grayscale photo of hands fitting puzzle pieces together"></div>
  <div class="back-wordmark">Tallowbrook Partners</div>
  <div class="name-band"></div>
  <div class="name">Dennis K. Holloway, MBA</div>
  <div class="title">Founder/President</div>
  <div class="address">5727 E. Larkspur Avenue,<br>Suite 418, Omaha, NE 68297</div>

  <div class="contact-row contact-row--phones">
    <span class="contact-item">
      <svg class="contact-icon" viewBox="0 0 24 24" aria-hidden="true"><path d="M6.6 10.8a15.1 15.1 0 0 0 6.6 6.6l2.2-2.2a1 1 0 0 1 1-.25 11.4 11.4 0 0 0 3.6.57 1 1 0 0 1 1 1V20a1 1 0 0 1-1 1A17 17 0 0 1 3 4a1 1 0 0 1 1-1h3.5a1 1 0 0 1 1 1c0 1.25.2 2.45.57 3.57a1 1 0 0 1-.25 1z"/></svg>
      : (402) 555-0147
    </span>
    <span class="contact-item">
      <svg class="contact-icon" viewBox="0 0 24 24" aria-hidden="true"><path d="M6 2h12v5H6zM3 8h18a1 1 0 0 1 1 1v7h-4v5H6v-5H2V9a1 1 0 0 1 1-1zm5 7v4h8v-4z"/></svg>
      : (402) 555-0129
    </span>
  </div>

  <div class="contact-bar"></div>
  <div class="contact-row contact-row--bar">
    <span class="contact-item">
      <svg class="contact-icon" viewBox="0 0 24 24" aria-hidden="true"><path d="M7 1h10a2 2 0 0 1 2 2v18a2 2 0 0 1-2 2H7a2 2 0 0 1-2-2V3a2 2 0 0 1 2-2zm0 3v14h10V4z"/></svg>
      : (402) 555-0183
    </span>
    <span class="contact-item">
      <svg class="contact-icon" viewBox="0 0 24 24" aria-hidden="true"><path d="M2 4h20v16H2zm2 2v.5l8 5 8-5V6zm0 2.8V18h16V8.8l-8 5z"/></svg>
      : dennis@tallowbrookgroup.example
    </span>
  </div>
</section>

</body>
</html>
```